New Business Card for Auto Repair and Performance Shop!

Need a redesign on a card that we have used for a while now. Something more update and modern, Serious but not too serious. Something confident, that shows the client that we are bespoke. Adding value.

Target Market(s)

Foreign Auto Repair and Performance

Industry/Entity Type

Automotive

Contact Information for Business Card

Utilize Logo, would like to change car silhouette to something Veltra,

Font styles to use
Sans Serif

Requirements
Must have
• business name, address, website, phone number.
MotoSerenix
4918 W. Birchwell Rd
Killeen, T.X. 76542
1-254-487-3106
www.moto-serenix-example.com

Specializing in Asian, European, and Domestic Auto Repair, Performance and Fabrication.

Clear space on back to for space to write appointment time and which client advisor helped the client.
Nice to have
• Up to the designers,

```html
<!DOCTYPE html>
<html lang="en">
<head>
<meta charset="utf-8">
<title>MotoSerenix Business Card</title>
<link rel="stylesheet" href="https://fonts.googleapis.com/css2?family=Saira+Semi+Condensed:wght@600&family=Share+Tech+Mono&display=swap">
<style>
  :root {
    --card-black: #000000;
    --ink-white: #f2f2f2;
    --accent-orange: #ff4a0f;
    --accent-orange-deep: #e63f0a;
    --steel: #b8b8b8;
    --ghost: #151515;
  }
  * { margin: 0; padding: 0; box-sizing: border-box; }
  html, body {
    width: 1200px;
    height: 685px;
    overflow: hidden;
    background: var(--card-black);
  }
  .card {
    position: relative;
    width: 1200px;
    height: 685px;
    background: var(--card-black);
    overflow: hidden;
  }
  .ghost-ring {
    position: absolute;
    left: 60px;
    top: 58px;
    width: 565px;
    height: 565px;
    border-radius: 50%;
    border: 34px solid var(--ghost);
  }
  .brand-name {
    position: absolute;
    left: 62px;
    top: 206px;
    font-family: "Saira Semi Condensed", sans-serif;
    font-weight: 600;
    font-size: 66px;
    line-height: 1;
    letter-spacing: 4px;
    text-transform: uppercase;
    color: var(--ink-white);
  }
  .brand-name .brand-accent { color: var(--accent-orange); }
  .contact-list {
    position: absolute;
    left: 92px;
    top: 308px;
    list-style: none;
  }
  .contact-item {
    display: flex;
    align-items: center;
    height: 30px;
    margin-bottom: 31px;
    font-family: "Share Tech Mono", monospace;
    font-size: 26px;
    letter-spacing: 1px;
    text-transform: uppercase;
    color: var(--ink-white);
  }
  .contact-icon {
    width: 28px;
    height: 28px;
    border-radius: 6px;
    background: var(--accent-orange);
    margin-right: 28px;
    display: flex;
    align-items: center;
    justify-content: center;
    flex-shrink: 0;
  }
  .contact-icon svg { width: 20px; height: 20px; }
  .brand-mark {
    position: absolute;
    left: 805px;
    top: 212px;
    width: 296px;
    height: 296px;
    border-radius: 50%;
    border: 16px solid var(--steel);
    display: flex;
    align-items: center;
    justify-content: center;
  }
  .brand-mark-name {
    font-family: "Saira Semi Condensed", sans-serif;
    font-weight: 600;
    font-size: 38px;
    letter-spacing: 1px;
    color: var(--accent-orange);
  }
  .tagline {
    position: absolute;
    left: 63px;
    top: 592px;
    font-family: "Saira Semi Condensed", sans-serif;
    font-weight: 600;
    font-size: 13px;
    letter-spacing: 3.3px;
    text-transform: uppercase;
    color: var(--ink-white);
  }
  .accent-rule {
    position: absolute;
    left: 0;
    top: 627px;
    width: 1200px;
    height: 8px;
    background: var(--accent-orange-deep);
  }
</style>
</head>
<body>
<main class="card">
  <div class="ghost-ring" aria-hidden="true"></div>

  <h1 class="brand-name">Moto<span class="brand-accent">Serenix</span></h1>

  <ul class="contact-list">
    <li class="contact-item">
      <span class="contact-icon">
        <svg viewBox="0 0 24 24" aria-hidden="true"><path d="M12 2a7 7 0 0 0-7 7c0 5 7 13 7 13s7-8 7-13a7 7 0 0 0-7-7z" fill="none" stroke="#000" stroke-width="2.4"/><circle cx="12" cy="9" r="2.5" fill="#000"/></svg>
      </span>
      4918 W. Birchwell Rd Killeen, T.X. 76542
    </li>
    <li class="contact-item">
      <span class="contact-icon">
        <svg viewBox="0 0 24 24" aria-hidden="true"><path d="M6.6 2.5l3 .5 1.4 4.5-2.2 1.8a12 12 0 0 0 6 6l1.8-2.2 4.5 1.4.5 3c0 1.5-1.3 2.5-2.7 2.5C10.4 20 4 13.6 4 5.2 4 3.8 5.1 2.5 6.6 2.5z" fill="#000"/></svg>
      </span>
      1-254-487-3106
    </li>
    <li class="contact-item">
      <span class="contact-icon">
        <svg viewBox="0 0 24 24" aria-hidden="true" fill="none" stroke="#000" stroke-width="2"><circle cx="12" cy="12" r="9"/><ellipse cx="12" cy="12" rx="4" ry="9"/><path d="M3 12h18M5 7h14M5 17h14"/></svg>
      </span>
      www.moto-serenix-example.com
    </li>
  </ul>

  <div class="brand-mark">
    <span class="brand-mark-name">MotoSerenix</span>
  </div>

  <p class="tagline">Specializing in Asian, European, and Domestic Auto Repair, Performance and Fabrication.</p>
  <div class="accent-rule" aria-hidden="true"></div>
</main>
</body>
</html>
```